Fernvale Business Card Design

We are looking for a fresh business card design for our new logo. We would like a business card that is unique but friendly. We are in the window coverings business offering blinds, shutters and shades for homes.

Target Market(s)

Targeting the end-consumer

Industry/Entity Type

Business

Requirements
Must have
• Must have a dedicates space for a photo of our sales person. Must contain our new logo (attached).

```html
<!DOCTYPE html>
<html lang="en">
<head>
<meta charset="utf-8">
<title>Fernvale Business Card</title>
<link href="https://fonts.googleapis.com/css2?family=Lato:wght@400;700&display=swap" rel="stylesheet">
<style>
  :root {
    --backdrop: #a3a3a3;
    --card: #f2f2f2;
    --ink: #3a3a3a;
    --brand-grey: #6b6b6b;
    --leaf-green: #8cc63f;
    --bar-grey: #a9a9a9;
    --photo-light: #d9dde2;
    --photo-dark: #4b5663;
  }
  * { box-sizing: border-box; margin: 0; padding: 0; }
  html, body { width: 1200px; height: 1004px; overflow: hidden; }
  body {
    background: var(--backdrop);
    font-family: 'Lato', sans-serif;
    color: var(--ink);
    position: relative;
  }
  .card {
    position: absolute;
    left: 220px;
    width: 760px;
    height: 434px;
    background: var(--card);
    box-shadow: 0 6px 18px rgba(0,0,0,.18);
  }
  .card--back { top: 44px; }
  .card--front { top: 526px; }

  /* back side */
  .back-bar {
    position: absolute; left: 0; top: 210px;
    width: 190px; height: 12px; background: var(--leaf-green);
  }
  .back-line {
    position: absolute; left: 570px; right: 0; top: 215px;
    height: 2px; background: var(--leaf-green);
  }
  .brand {
    position: absolute;
    display: flex; align-items: center; gap: 16px;
    color: var(--brand-grey);
    font-weight: 400;
  }
  .brand-square {
    border: 3px solid var(--brand-grey);
    border-radius: 6px;
  }
  .card--back .brand { left: 214px; top: 180px; font-size: 52px; }
  .card--back .brand-square { width: 62px; height: 62px; }

  /* front side */
  .card--front .brand { left: 338px; top: 40px; font-size: 54px; }
  .card--front .brand-square { width: 80px; height: 80px; }

  .photo {
    position: absolute; left: 52px; top: 48px;
    width: 198px; height: 198px; border-radius: 50%;
    background: radial-gradient(circle at 50% 35%, var(--photo-light) 0%, #9aa6b2 55%, var(--photo-dark) 100%);
    box-shadow: inset 0 2px 6px rgba(0,0,0,.35);
  }
  .name-tag {
    position: absolute; left: 203px; top: 168px;
    width: 318px; height: 30px;
    background: var(--leaf-green);
    clip-path: polygon(6% 0, 100% 0, 94% 100%, 0 100%);
    color: #fff; font-weight: 700; font-size: 22px; letter-spacing: .5px;
    display: flex; align-items: center; justify-content: center;
  }
  .position-tag {
    position: absolute; left: 142px; top: 210px;
    width: 274px; height: 26px;
    background: var(--bar-grey);
    clip-path: polygon(0 0, 100% 0, 95% 100%, 0 100%);
    color: #fff; font-size: 18px;
    display: flex; align-items: center; justify-content: center;
  }
  .front-bar {
    position: absolute; left: 0; top: 264px;
    width: 307px; height: 13px; background: var(--leaf-green);
  }
  .front-line {
    position: absolute; left: 307px; right: 0; top: 270px;
    height: 2px; background: var(--leaf-green);
  }
  .contact {
    position: absolute; top: 300px;
    list-style: none; font-size: 19px;
  }
  .contact li { height: 36px; display: flex; align-items: center; gap: 12px; }
  .contact--web { left: 62px; }
  .contact--phones { right: 54px; }
  .contact--phones li { justify-content: flex-end; }
  .icon { width: 18px; height: 18px; fill: var(--ink); flex: none; }
</style>
</head>
<body>

<section class="card card--back" aria-label="Card back">
  <div class="back-bar"></div>
  <div class="brand"><span class="brand-square"></span><span class="brand-name">Fernvale</span></div>
  <div class="back-line"></div>
</section>

<section class="card card--front" aria-label="Card front">
  <div class="photo" role="img" aria-label="Portrait photo of the sales person"></div>
  <div class="brand"><span class="brand-square"></span><span class="brand-name">Fernvale</span></div>
  <div class="name-tag">NAME SURNAME</div>
  <div class="position-tag">Position</div>
  <div class="front-bar"></div>
  <div class="front-line"></div>

  <ul class="contact contact--web">
    <li>
      <svg class="icon" viewBox="0 0 18 18"><path d="M1 2h16v11H1z M3 4v7h12V4z M6 15h6v2H6z" fill-rule="evenodd"/></svg>
      www.website.com
    </li>
    <li>
      <svg class="icon" viewBox="0 0 18 18"><path d="M1 4h16v11H1z"/><path d="M1 4l8 6 8-6" fill="none" stroke="#f2f2f2" stroke-width="1.5"/></svg>
      info@website.com
    </li>
    <li>
      <svg class="icon" viewBox="0 0 18 18"><path d="M9 1a6 6 0 0 1 6 6c0 4-6 10-6 10S3 11 3 7a6 6 0 0 1 6-6z"/><circle cx="9" cy="7" r="2.2" fill="#f2f2f2"/></svg>
      12 Maple Row, Brookside 54321, USA
    </li>
  </ul>

  <ul class="contact contact--phones">
    <li>+1 012 345 6789
      <svg class="icon" viewBox="0 0 18 18"><path d="M4 1l3 4-2 2c1 2 3 4 5 5l2-2 4 3-2 3C8 16 2 10 1 4z"/></svg>
    </li>
    <li>+1 987 654 3210
      <svg class="icon" viewBox="0 0 18 18"><path d="M5 1h8v4H5z M2 6h14v7h-3v-2H5v2H2z M6 12h6v5H6z"/></svg>
    </li>
    <li>+1 098 765 4321
      <svg class="icon" viewBox="0 0 18 18"><path d="M5 1h8v16H5z M6.5 3v10h5V3z" fill-rule="evenodd"/></svg>
    </li>
  </ul>
</section>

</body>
</html>
```